Flyer-Design
Zielgruppe
Ich bin gelernte Bankkauffrau, Dipl. Betriebswirtin, geprüfte Immobilienberaterin sowie Bausachverständige für Immobilienbewertung. Nach mehr als 30 Jahren Tätigkeit als Immobilienmaklerin für diverse Banken und große Maklerunternehmen, habe ich zum 01.01.2022 meine eigene Firma, die Tarvo Immobilienberatung GmbH & Co. KG gegründet.
Da Großunternehmen sehr unflexibel und träge sind und man dadurch nicht auf alle Bedürfnisse des Kunden so eingehen kann, wie ich es mir für meine Kunden wünsche, habe ich meine eigene Firma gegründet. Überschaubar groß, flexibel und Kundennah. Bei uns steht der Mensch mit all seinen Emotionen rund um den Immobilienverkauf im Vordergrund.
Wir bieten zusätzlich zum klassischen rundum-sorglos Immobilienverkauf von Bestandsimmobilien, auch Honorarberatung für Immobilien Selbstverkäufer an. Darüber hinaus auch Baufinanzierungen.
Unsere Zielgruppe sind verkaufsbereite Immobilieneigentümer jeglichen Alters. Meistens sind die Verkäufer jedoch im fortgeschrittenen Alter. Sowie Immobilienkäufer, die eine Finanzierung benötigen.
Aufgabenstellung
Er soll zum Design unserer Homepage passen www.tarvo-immobilien-beispiel.de.
Die Flyer sollen zum Auslegen, zur Mitnahme aus Hängeboxen und zum Briefkasteneinwurf dienen, um unsere Firma bekannt zu machen und Aufträge zu generieren.
Modern, aber nicht zu flippig/unruhig. Er muss die ältere Generation mit Bild und Text emotional ansprechen und Sicherheit vermitteln, aber auch die 30-40 Jährigen. Er soll sich von den üblichen, langweiligen Maklerflyern abheben.
Den Flyer wünschen wir uns später auch in DIN A4 Format zur Übergabe beim Kunden in einer Mappe.

```html
<!DOCTYPE html>
<html lang="de">
<head>
<meta charset="utf-8">
<title>Tarvo Immobilienberatung – Flyer</title>
<link href="https://fonts.googleapis.com/css2?family=League+Spartan:wght@800&family=Montserrat:wght@400;500&display=swap" rel="stylesheet">
<style>
  :root {
    --navy: #1c2060;
    --beige: #dccab5;
    --tan: #c49a6c;
    --white: #ffffff;
    --rule: #f4ede4;
  }
  * { margin: 0; padding: 0; box-sizing: border-box; }
  html, body { width: 867px; height: 1200px; overflow: hidden; background: var(--white); }
  .flyer { position: relative; width: 867px; height: 1200px; overflow: hidden; background: var(--white); font-family: "Montserrat", sans-serif; color: var(--navy); }

  .brand { position: absolute; left: 40px; top: 16px; display: flex; align-items: center; gap: 12px; }
  .brand-square { width: 36px; height: 36px; background: var(--tan); }
  .brand-name { font-family: "League Spartan", sans-serif; font-weight: 800; font-size: 46px; letter-spacing: 1px; color: var(--navy); line-height: 1; padding-top: 6px; }

  .panel { position: absolute; left: 138px; top: 89px; right: 0; bottom: 0; background: var(--beige); }

  .headline { position: absolute; left: 192px; top: 116px; font-family: "League Spartan", sans-serif; font-weight: 800; font-size: 38px; line-height: 44px; color: var(--navy); text-transform: uppercase; }
  .tagline { position: absolute; left: 192px; top: 209px; font-size: 26px; font-weight: 400; color: var(--white); letter-spacing: 0.8px; text-transform: uppercase; }

  .photo { position: absolute; left: 0; top: 279px; width: 867px; height: 412px;
    background: linear-gradient(180deg, #c7d6e0 0%, #dfe4e4 28%, #a9b8a0 40%, #c7a07e 55%, #5fa6b4 70%, #b98a6c 85%, #9b8a7a 100%); }
  .photo-tint { position: absolute; left: 138px; top: 279px; width: 729px; height: 412px; background: rgba(220, 202, 181, 0.55); }

  .services { position: absolute; left: 192px; top: 732px; width: 226px; list-style: none; }
  .service { font-size: 18.5px; font-weight: 500; letter-spacing: 0.9px; line-height: 26px; text-transform: uppercase; color: var(--navy); padding-bottom: 20px; margin-bottom: 16px; border-bottom: 2px solid var(--rule); white-space: nowrap; }
  .service:last-child { border-bottom: none; }

  .intro { position: absolute; left: 463px; top: 733px; width: 368px; font-size: 13.4px; line-height: 19.7px; text-align: justify; color: var(--navy); }
  .intro p { margin-bottom: 19.7px; }
  .signature { position: absolute; left: 463px; top: 1146px; font-size: 13.6px; font-weight: 500; color: var(--navy); }

  .contact { position: absolute; left: 20px; bottom: 36px; transform-origin: left bottom; transform: rotate(-90deg) translateX(-0px); width: 480px; display: flex; gap: 22px; font-size: 13px; line-height: 19px; color: var(--navy); }
  .contact-block { display: flex; flex-direction: column; }
</style>
</head>
<body>
<div class="flyer">
  <div class="brand">
    <span class="brand-square"></span>
    <span class="brand-name">TARVO</span>
  </div>

  <div class="panel"></div>

  <h1 class="headline">Ihr Immobilienprofi für<br>Rhein-Neckar und die Pfalz</h1>
  <p class="tagline">Für Ihre Immobilie nur das Beste</p>

  <div class="photo" role="img" aria-label="Luftbild einer Stadt am Fluss mit Brücke, Altstadtdächern und bewölktem Himmel"></div>
  <div class="photo-tint" aria-hidden="true"></div>

  <ul class="services">
    <li class="service">Rundum-Sorglos<br>Immobilienverkauf</li>
    <li class="service">Honorarberatung<br>für Selbstverkäufer</li>
    <li class="service">Immobilien-<br>bewertung</li>
    <li class="service">Bonitätsprüfung</li>
    <li class="service">Finanzierungs-<br>vermittlung</li>
    <li class="service">Home Staging</li>
  </ul>

  <div class="intro">
    <p>Ihre Immobilie zu verkaufen, ist keine leichte Entscheidung und ein Verkauf keine einfache Aufgabe, denn jede Immobilie hat ihre eigene Geschichte. Es bedarf Marktkenntnis und lang&shy;jährige Erfahrung den passenden Käufer zum richtigen Preis zu finden.</p>
    <p>Wir sagen Ihnen nicht nur, was Ihre Immobilie wert ist, sondern entwickeln mit Ihnen die richtige Strategie, um Ihre Immobilie schnell und nach Ihren Bedürfnissen zu veräußern.</p>
    <p>Oder sind Sie noch immer auf der Suche nach Ihrem neuen Zuhause? Wir lassen Sie nicht alleine und begeben uns für Sie auf die Suche.</p>
    <p>Nehmen Sie gerne Kontakt mit uns auf und lernen Sie unsere Schritte zu einer professionellen Vermarktung kennen. Wir freuen uns auf Sie!</p>
  </div>
  <p class="signature">Helene Marquardt &amp; Jonas Wendler</p>

  <div class="contact">
    <div class="contact-block">
      <span>Tarvo Immobilienberatung GmbH &amp; Co. KG</span>
      <span>Lindenweg 12, 68159 Mannheim</span>
    </div>
    <div class="contact-block">
      <span>+49 (0)621 – 40057720</span>
      <span>kontakt@tarvo-immobilien-beispiel.de · www.tarvo-immobilien-beispiel.de</span>
    </div>
  </div>
</div>
</body>
</html>
```